Business cards for a recruitment company
Marrowby Associates
Modern
Helena Marrowby
Managing Director
PO Box 48213 Corvel Harbour Plaza Dubai United Arab Emirates
lena@marrowbyassociates-mail.test
marrowbyassociates-mail.test
The business card needs to have my name, designation etc in both English and Arabic. Therefore, both languages will appear on the front of the card. The final design will illustrate how two different translations will appear on the front of the card. **The logo must also appear on the front of the card.
The back of the card will be plain white with just the logo as attached in the AI file. Perhaps the logo could be indented.

```html
<!DOCTYPE html>
<html lang="en">
<head>
<meta charset="utf-8">
<title>Marrowby Associates – Business Cards</title>
<link href="https://fonts.googleapis.com/css2?family=Open+Sans:wght@400;600&family=Cairo:wght@400;600&display=swap" rel="stylesheet">
<style>
  :root{
    --stage:#5b5b5b;
    --ink:#141414;
    --paper:#ffffff;
    --paper-shade:#d9d9d9;
    --violet:#8b5aa0;
    --muted:#a9a9a9;
    --soft-white:#f2f2f2;
  }
  *{box-sizing:border-box;margin:0;padding:0}
  html,body{width:1200px;height:895px;overflow:hidden;background:var(--stage)}
  body{position:relative;font-family:"Open Sans",Arial,sans-serif}

  .card{position:absolute;left:250px;width:700px;height:400px;overflow:hidden;box-shadow:0 8px 24px rgba(0,0,0,.35)}
  .card--front{top:30px}
  .card--back{top:465px}
  .card__shape{position:absolute;inset:0;width:100%;height:100%}

  .brand{position:absolute;display:flex;flex-direction:column;align-items:center;text-align:center}
  .brand__mark{width:38px;height:38px;border-radius:50%;background:var(--violet);margin-bottom:14px}
  .brand__name{font-weight:600;font-size:30px;letter-spacing:2px;line-height:1.05;text-transform:uppercase}
  .brand__name span{display:block;font-size:16px;letter-spacing:7px;margin-top:6px}
  .brand--dark{left:40px;top:120px;width:230px;color:var(--ink)}
  .brand--light{left:0;top:55px;width:700px;color:var(--paper)}

  .details{position:absolute;right:34px;top:40px;width:300px;text-align:right;color:var(--soft-white)}
  .details__name{color:var(--violet);font-size:14px;font-weight:600;letter-spacing:1.5px;text-transform:uppercase}
  .details__role{color:var(--muted);font-size:11px;margin-top:2px}
  .details__arabic{font-family:"Cairo","Noto Naskh Arabic",sans-serif;direction:rtl;margin-top:14px;line-height:1.35}
  .details__arabic .ar-name{font-size:23px;color:var(--violet)}
  .details__arabic .ar-role{font-size:17px;color:var(--paper)}
  .details__address{font-size:11px;line-height:1.6;margin-top:16px;color:var(--soft-white)}
  .contact{list-style:none;margin-top:16px}
  .contact li{display:flex;justify-content:flex-end;align-items:center;gap:8px;font-size:11px;line-height:20px;color:var(--soft-white)}
  .contact svg{width:12px;height:12px;fill:var(--muted)}

  .website{position:absolute;left:0;bottom:42px;width:700px;text-align:center;font-size:19px;letter-spacing:5px;color:#3a3a3a}
</style>
</head>
<body>

<section class="card card--front" aria-label="Business card front">
  <svg class="card__shape" viewBox="0 0 700 400" aria-hidden="true">
    <defs>
      <linearGradient id="paperFront" x1="0" y1="0" x2="1" y2="1">
        <stop offset="0" stop-color="#ffffff"/>
        <stop offset="1" stop-color="#dcdcdc"/>
      </linearGradient>
    </defs>
    <rect width="700" height="400" fill="#141414"/>
    <path d="M0 0 H310 C400 110 400 290 310 400 H0 Z" fill="#8b5aa0"/>
    <path d="M0 0 H298 C386 110 386 290 298 400 H0 Z" fill="url(#paperFront)"/>
  </svg>

  <div class="brand brand--dark">
    <div class="brand__mark"></div>
    <div class="brand__name">Marrowby<span>Associates</span></div>
  </div>

  <div class="details">
    <p class="details__name">Helena Marrowby</p>
    <p class="details__role">Managing Director</p>
    <div class="details__arabic" lang="ar">
      <p class="ar-name">هيلينا ماروبي</p>
      <p class="ar-role">المدير العام</p>
    </div>
    <p class="details__address">PO Box 48213 Corvel Harbour Plaza<br>Dubai, United Arab Emirates</p>
    <ul class="contact">
      <li>012 345 6789
        <svg viewBox="0 0 24 24"><path d="M6.6 10.8a15 15 0 0 0 6.6 6.6l2.2-2.2a1 1 0 0 1 1-.25 11.4 11.4 0 0 0 3.6.57 1 1 0 0 1 1 1V20a1 1 0 0 1-1 1A17 17 0 0 1 3 4a1 1 0 0 1 1-1h3.5a1 1 0 0 1 1 1c0 1.25.2 2.45.57 3.57a1 1 0 0 1-.25 1z"/></svg></li>
      <li>012 345 6789
        <svg viewBox="0 0 24 24"><path d="M7 1h10a2 2 0 0 1 2 2v18a2 2 0 0 1-2 2H7a2 2 0 0 1-2-2V3a2 2 0 0 1 2-2zm0 3v14h10V4z"/></svg></li>
      <li>012 345 6789
        <svg viewBox="0 0 24 24"><path d="M6 2h12v6H6zM3 9h18a1 1 0 0 1 1 1v7h-4v5H6v-5H2v-7a1 1 0 0 1 1-1zm5 6v5h8v-5z"/></svg></li>
      <li>lena@marrowbyassociates-mail.test
        <svg viewBox="0 0 24 24"><path d="M2 5h20v14H2zm2 2v.5l8 5 8-5V7z"/></svg></li>
      <li>marrowbyassociates-mail.test
        <svg viewBox="0 0 24 24"><path d="M12 2a10 10 0 1 0 0 20 10 10 0 0 0 0-20zm-1 3v5H6.1A8 8 0 0 1 11 5zm2 0a8 8 0 0 1 4.9 5H13zm-6.9 7H11v5a8 8 0 0 1-4.9-5zM13 12h4.9A8 8 0 0 1 13 17z"/></svg></li>
    </ul>
  </div>
</section>

<section class="card card--back" aria-label="Business card back">
  <svg class="card__shape" viewBox="0 0 700 400" aria-hidden="true">
    <defs>
      <linearGradient id="paperBack" x1="0" y1="0" x2="0" y2="1">
        <stop offset="0" stop-color="#ffffff"/>
        <stop offset="1" stop-color="#d4d4d4"/>
      </linearGradient>
    </defs>
    <rect width="700" height="400" fill="url(#paperBack)"/>
    <path d="M0 0 H700 V205 C520 305 200 300 0 215 Z" fill="#8b5aa0"/>
    <path d="M0 0 H700 V192 C520 290 200 285 0 202 Z" fill="#141414"/>
  </svg>

  <div class="brand brand--light">
    <div class="brand__mark"></div>
    <div class="brand__name">Marrowby<span>Associates</span></div>
  </div>

  <p class="website">www.marrowbyassociates-mail.test</p>
</section>

</body>
</html>
```